Bramblewick Co Leaflet. A5 2-sided Flyer for a UK Lawn Treatment Company

I need an A5 two-side leaflet / flyer designed for my Lawn Treatment company. The leaflet will be for door-drops so quick impact needed. Full colour, both sides. I provide lawn treatments to customers in the Exeter area of Devon. I would like to design to be clear, fresh and reflect the joy a good lawn and garden can bring.

Target Market(s)

Home Owners. 30-80 Years. Familys

Font styles to use
Sans Serif

Colors
9bcb3c
f78f20
ec1f27
33a6d7

Requirements
Must have
• Good front page picture
• Logo
• Contact details on front.
• Call to Action
• More details in Text file included in design.
Nice to have
• Clipart of a family / lady enjoying a lawn.

```html
<!DOCTYPE html>
<html lang="en">
<head>
<meta charset="utf-8">
<title>Bramblewick Co Leaflet</title>
<link href="https://fonts.googleapis.com/css2?family=Roboto+Slab:wght@300;400;500&display=swap" rel="stylesheet">
<style>
  :root{
    --bg:#e6e3df;
    --paper:#f1f1f0;
    --paper-back:#e9e8e6;
    --green:#3e9a3c;
    --green-dark:#2f7f34;
    --red:#d8434a;
    --brown:#7b3a2c;
    --brown-dark:#6a3024;
    --yellow:#f2c341;
    --blue:#4a86c2;
    --blue-light:#5a96cf;
    --white:#ffffff;
  }
  *{box-sizing:border-box;margin:0;padding:0}
  html,body{width:1200px;height:900px;overflow:hidden}
  body{background:var(--bg);font-family:"Roboto Slab",Georgia,serif;position:relative}
  .page{position:absolute;top:50px;width:566px;height:800px;overflow:hidden;box-shadow:0 4px 14px rgba(0,0,0,.18)}
  .front{left:22px;background:var(--paper)}
  .back{left:612px;background:var(--paper-back)}

  /* front */
  .brand{position:absolute;top:34px;left:0;right:0;display:flex;justify-content:center;align-items:center;gap:12px}
  .brand-dot{width:34px;height:34px;border-radius:50%;background:var(--green)}
  .brand-name{font-size:30px;font-weight:400;color:var(--green);letter-spacing:1px}
  .headlines{position:absolute;top:118px;left:26px;right:24px;text-transform:uppercase}
  .tagline{font-size:15.5px;font-weight:300;color:var(--green);white-space:nowrap}
  .hero{font-size:38px;font-weight:400;color:var(--green);line-height:1.05;margin-top:4px;white-space:nowrap}
  .exp{font-size:14.5px;font-weight:300;color:var(--green);white-space:nowrap}
  .guarantee{font-size:27.5px;font-weight:400;color:var(--red);line-height:1.1;white-space:nowrap}
  .red{color:var(--red)}
  .front-art{position:absolute;left:0;top:0;width:566px;height:706px}
  .front-footer{position:absolute;left:0;bottom:0;width:566px;height:94px;background:var(--blue);border-top:6px solid var(--brown);color:var(--white);overflow:hidden}
  .footer-shade{position:absolute;right:0;top:0;width:300px;height:100%;background:var(--blue-light);clip-path:polygon(40% 0,100% 0,100% 100%,0 100%)}
  .footer-text{position:absolute;left:20px;top:10px;font-size:13px;font-weight:300;line-height:19px;text-transform:uppercase}
  .footer-text .web{margin-top:14px}
  .footer-brand{position:absolute;right:26px;top:34px;display:flex;align-items:center;gap:7px}
  .footer-brand .brand-dot{width:16px;height:16px;background:var(--green-dark)}
  .footer-brand .brand-name{font-size:16px;color:var(--green-dark)}

  /* back */
  .band{position:absolute;left:0;width:100%;height:22px;background:var(--brown)}
  .band.top{top:0}
  .band.bottom{bottom:0;background:var(--brown-dark)}
  .content{position:absolute;top:30px;left:12px;right:30px}
  .section h2{font-size:16px;font-weight:400;color:var(--brown);text-transform:uppercase;line-height:20px}
  .section p{font-size:11px;font-weight:300;color:var(--green);line-height:14px;margin-left:10px}
  .section{margin-bottom:12px}
  .treatments{list-style:none;margin:4px 0 4px 13px}
  .treatments li{font-size:11px;font-weight:300;color:var(--brown);line-height:14.5px;text-transform:uppercase}
  .testimonials{margin-top:24px;margin-left:6px}
  .testimonials h2{font-size:22px;font-weight:400;color:var(--brown);text-transform:uppercase;line-height:26px}
  .quote{font-size:13.5px;font-weight:300;color:var(--green);line-height:17.5px;margin:2px 0 12px 6px}
  .quote cite{font-style:normal;font-size:9.5px;color:var(--brown);margin-left:4px}
</style>
</head>
<body>

<section class="page front">
  <svg class="front-art" viewBox="0 0 566 706" aria-hidden="false">
    <path role="img" aria-label="Photograph of a sunny garden with a striped green lawn and flowering shrubs" d="M0 348 Q290 330 566 255 L566 706 L0 706 Z" fill="url(#gardenTone)"/>
    <defs>
      <linearGradient id="gardenTone" x1="0" y1="0" x2="0" y2="1">
        <stop offset="0" stop-color="#3c5a2a"/>
        <stop offset="0.45" stop-color="#5f8a3d"/>
        <stop offset="0.62" stop-color="#86b84a"/>
        <stop offset="1" stop-color="#74ac3c"/>
      </linearGradient>
    </defs>
    <path d="M0 332 Q290 316 566 238 L566 252 Q290 330 0 346 Z" fill="var(--green)"/>
    <path d="M0 346 Q290 330 566 252 L566 260 Q290 338 0 354 Z" fill="var(--yellow)"/>
  </svg>

  <div class="brand">
    <span class="brand-dot"></span>
    <span class="brand-name">Bramblewick Co</span>
  </div>

  <div class="headlines">
    <p class="tagline">Treatments and advice to keep your lawn looking <span class="red">nice.</span></p>
    <p class="hero"><span class="red">Brand new</span> to the area!</p>
    <p class="exp">8 years experience maintaining the finest lawns of <span class="red">Cheshire</span></p>
    <p class="guarantee">Complete satisfaction guarantee</p>
  </div>

  <footer class="front-footer">
    <div class="footer-shade"></div>
    <div class="footer-text">
      <p>Call today on 01392 517460 &nbsp;&nbsp; or text 07700 913528</p>
      <p>To book your lawn survey</p>
      <p class="web">www.bramblewickco.co.uk</p>
    </div>
    <div class="footer-brand">
      <span class="brand-dot"></span>
      <span class="brand-name">Bramblewick Co</span>
    </div>
  </footer>
</section>

<section class="page back">
  <div class="band top"></div>
  <div class="content">
    <div class="section">
      <h2>For a beautiful weed-free lawn</h2>
      <p>Call Bramblewick Co today and start your journey to a wonderful, lush, green lawn you and your family can enjoy. Arrange a no-obligation lawn survey and quotation at a time to suit you. Call 01392 517460 now.</p>
    </div>
    <div class="section">
      <h2>I will understand your lawn</h2>
      <p>Every lawn is unique. I take time to gain a comprehensive understanding of your lawn and its situation. I will also listen to you and understand your problems and your aspirations for your grass.</p>
    </div>
    <div class="section">
      <h2>Your lawn treatments</h2>
      <p>I will create a custom treatment programme tailored to your lawn. I may also recommend some remedial treatments to correct any existing problems. There is no contract to sign. I guarantee all treatments.</p>
    </div>
    <div class="section">
      <h2>Industry-leading lawn care</h2>
      <p>I have 8 years of experience in the leading edge of domestic lawn care. I have a comprehensive range of treatments including:</p>
      <ul class="treatments">
        <li>- Scarification</li>
        <li>- Aeration</li>
        <li>- Moss control</li>
        <li>- Overseeding</li>
        <li>- Top dressing</li>
        <li>- Lawn repairs</li>
        <li>- Fertilisation &amp; weed control</li>
        <li>- Pest and disease management</li>
        <li>- Special event preparation</li>
      </ul>
      <p>Save time and money and leave your lawn to an expert.</p>
    </div>

    <div class="testimonials">
      <h2>Testimonials</h2>
      <p class="quote">"Thank you for keeping our lawn in great shape for so long, I've been really pleased with how it has looked since you took care of it"<cite>Owen</cite></p>
      <p class="quote">"My lawn has never looked better since the day that you started to look after it for me"<cite>Mr. Pryce</cite></p>
      <p class="quote">"We are so grateful for your skill over the years. We've seen our lawn thrive and you changed a neglected difficult garden to one that everyone comments on"<cite>Carys</cite></p>
      <p class="quote">"Thank you for the lawn service you have provided over the years. It is reassuring to have you come round as I know you carried out the service as promised unlike other lawn service companies I have dealt with"<cite>Glen</cite></p>
    </div>
  </div>
  <div class="band bottom"></div>
</section>

</body>
</html>
```